deceased estate cleaning services and cosmetic renovating

house frontage signage design
cur flute sign will be 600mm x 450 mm and no larger
is to be mounted of fence out front of projects as advertizing

Target Market(s)

elderly people and there sibling that need help

Colors
cadf82
85cae6
fbed22
85acd3
ffcf3e

Requirements
Must have
• clear phone number, email and business Name and logo
Should not have
• to much info and NO dark colors

```html
<!DOCTYPE html>
<html lang="en">
<head>
<meta charset="utf-8">
<title>Tidywell – De-Clutter Your Life</title>
<link rel="stylesheet" href="https://fonts.googleapis.com/css2?family=Crimson+Pro:ital,wght@0,500;0,600;0,700;1,500;1,600&display=swap">
<style>
  :root {
    --sky: #85acd3;
    --leaf: #78a55a;
    --leaf-light: #a9cc72;
    --sun: #fbed22;
    --amber: #ffcf3e;
    --ink: #111111;
    --paper: #ffffff;
    --tag-blue: #7ea3d0;
  }
  html, body {
    margin: 0;
    padding: 0;
    overflow: hidden;
    background: var(--paper);
  }
  .sign {
    display: block;
    width: 1200px;
    height: 800px;
    font-family: "Crimson Pro", Georgia, serif;
  }
  .bubble-sky { fill: var(--sky); }
  .bubble-leaf { fill: var(--leaf); }
  .bubble-sun { fill: var(--sun); }
  .bubble-amber { fill: var(--amber); }
  .mount-hole { fill: var(--paper); stroke: #9a9a9a; stroke-width: 1; }
  .headline { fill: var(--paper); font-size: 78px; font-weight: 600; }
  .enquiry { fill: var(--paper); font-size: 33px; font-style: italic; font-weight: 500; }
  .phone { fill: var(--paper); font-size: 54px; font-style: italic; font-weight: 600; }
  .contact-line { fill: var(--paper); font-size: 35px; font-style: italic; font-weight: 500; }
  .value-item { fill: var(--ink); font-size: 51px; font-weight: 700; }
  .value-dot { fill: var(--leaf); }
  .brand-name { fill: var(--ink); font-size: 64px; font-weight: 600; letter-spacing: 5px; }
  .brand-mark { fill: var(--leaf-light); }
  .brand-tagline { fill: var(--tag-blue); font-size: 48px; font-style: italic; font-weight: 600; }
  .services { fill: var(--paper); font-size: 43px; font-weight: 600; }
  .eco-name { fill: var(--ink); font-size: 38px; font-weight: 600; letter-spacing: 2px; }
  .eco-tagline { fill: var(--paper); font-size: 22px; font-style: italic; font-weight: 500; }
  .eco-slogan { fill: var(--paper); font-size: 60px; font-weight: 600; }
  .recycle-art { fill: var(--leaf-light); }
  .heart { fill: var(--paper); }
</style>
</head>
<body>
<svg class="sign" viewBox="0 0 1200 800" xmlns="http://www.w3.org/2000/svg">
  <defs>
    <filter id="lift" x="-10%" y="-10%" width="120%" height="120%">
      <feDropShadow dx="0" dy="2" stdDeviation="2" flood-color="#000" flood-opacity="0.35"/>
    </filter>
    <linearGradient id="recycleFill" x1="0" y1="0" x2="0" y2="1">
      <stop offset="0" stop-color="#8fb95e"/>
      <stop offset="1" stop-color="#b7d47a"/>
    </linearGradient>
  </defs>

  <g class="backdrop" filter="url(#lift)">
    <ellipse class="bubble-amber" cx="300" cy="-40" rx="400" ry="240" transform="rotate(-10 300 -40)"/>
    <ellipse class="bubble-sky" cx="240" cy="-45" rx="365" ry="255"/>
    <ellipse class="bubble-sun" cx="900" cy="300" rx="505" ry="215" transform="rotate(-12 900 300)"/>
    <ellipse class="bubble-leaf" cx="943" cy="138" rx="320" ry="220"/>
    <ellipse class="bubble-sun" cx="700" cy="830" rx="230" ry="140"/>
    <ellipse class="bubble-leaf" cx="218" cy="820" rx="340" ry="228"/>
    <ellipse class="bubble-sky" cx="965" cy="770" rx="350" ry="365"/>
  </g>

  <g class="mount-holes">
    <circle class="mount-hole" cx="36" cy="33" r="17"/>
    <circle class="mount-hole" cx="1157" cy="33" r="17"/>
    <circle class="mount-hole" cx="35" cy="749" r="17"/>
    <circle class="mount-hole" cx="1157" cy="756" r="17"/>
  </g>

  <g class="headline-block">
    <text class="headline" x="76" y="83">De-Clutter</text>
    <text class="headline" x="84" y="153">Your Life</text>
  </g>

  <g class="contact-block" text-anchor="end">
    <text class="enquiry" x="1119" y="54">If you have any queries</text>
    <text class="enquiry" x="1119" y="96">Get in touch with us.</text>
    <text class="phone" x="1119" y="164">Call 0400 123 456</text>
    <text class="contact-line" x="1119" y="207">hello@tidywell.com.au</text>
    <text class="contact-line" x="1119" y="249">www.tidywell.com.au</text>
  </g>

  <g class="values-list">
    <circle class="value-dot" cx="491" cy="218" r="7"/>
    <text class="value-item" x="507" y="236">Pride</text>
    <circle class="value-dot" cx="491" cy="279" r="7"/>
    <text class="value-item" x="507" y="297">Quality</text>
    <circle class="value-dot" cx="491" cy="341" r="7"/>
    <text class="value-item" x="507" y="359">Reliability</text>
    <circle class="value-dot" cx="491" cy="403" r="7"/>
    <text class="value-item" x="507" y="421">Professionalism</text>
  </g>

  <g class="brand-block" text-anchor="middle">
    <circle class="brand-mark" cx="237" cy="340" r="80"/>
    <text class="brand-name" x="237" y="506">TIDYWELL</text>
    <text class="brand-tagline" x="237" y="560">We’re here to help</text>
  </g>

  <g class="services-block">
    <text class="services" x="76" y="657">Cosmetic</text>
    <text class="services" x="76" y="706">Repairs &amp; House</text>
    <text class="services" x="76" y="755">Maintenance</text>
  </g>

  <g class="eco-block">
    <text class="eco-name" x="1119" y="490" text-anchor="end">TIDYWELL</text>
    <text class="eco-tagline" x="1119" y="519" text-anchor="end">Helping you to help</text>
    <text class="eco-tagline" x="1119" y="541" text-anchor="end">our environment.</text>
    <rect class="recycle-art" x="742" y="510" width="208" height="200" rx="60" fill="url(#recycleFill)" role="img" aria-label="Green recycling arrows symbol"/>
    <path class="heart" d="M1053 700 C1030 675 990 645 990 612 C990 595 1004 586 1020 586 C1036 586 1047 595 1053 606 C1059 595 1070 586 1086 586 C1102 586 1116 595 1116 612 C1116 645 1076 675 1053 700 Z"/>
    <text class="eco-slogan" x="1119" y="755" text-anchor="end">Recycle for life</text>
  </g>
</svg>
</body>
</html>
```